Prominent Law Firm Needs a New Stationary Design

We need new stationary design to go with our new logo and rustic offices.
Things we need on the letterhead:
logo (see attached file), would also like the Seven-Figure Verdict Logo (attached) somewhere on the stationary,
5182 North Pelham Avenue
Tulsa, Oklahoma 74219
(918) 555-0143 Tel ★ (918) 555-0187 Fax
www.TWVQX.example

We also need the names of the 4 partners:
Dale K. Hollingsworth
Vernon P. Hollingsworth
Mark E. Fenwicke
Tyler D. Ashcombe

And the other staff:
Brenda K. Lyle
Tendaji K. Oyelowanta
Gordon Pettijo

Hilda V. Pruitt, RN

Of Counsel:
Wendell S. Hollingsworth

Industry/Entity Type

Law Firm

```html
<!DOCTYPE html>
<html lang="en">
<head>
<meta charset="utf-8">
<title>Hollingsworth Hollingsworth Fenwicke – Stationery</title>
<link rel="stylesheet" href="https://fonts.googleapis.com/css2?family=Open+Sans:wght@400;600&family=Roboto:wght@400;500;700&display=swap">
<style>
  :root {
    --backdrop: #c5c6c8;
    --paper: #ffffff;
    --sidebar: #e6e7e9;
    --ink: #1f1f1f;
    --muted: #55585c;
    --watermark: #e2e2e2;
    --badge: #7a1620;
    --signature: #d7e3f1;
    --shadow: rgba(0,0,0,0.45);
  }
  * { box-sizing: border-box; margin: 0; padding: 0; }
  html, body { width: 1200px; height: 640px; overflow: hidden; background: var(--backdrop); }
  .board { position: relative; width: 1200px; height: 640px; }
  .sheet { position: absolute; background: var(--paper); box-shadow: 12px 14px 16px var(--shadow); overflow: hidden; }

  /* Letterhead */
  .letterhead { left: 72px; top: 42px; width: 430px; height: 556px; font-family: "Open Sans", sans-serif; color: var(--ink); }
  .sidebar { position: absolute; left: 0; top: 0; width: 90px; height: 100%; background: var(--sidebar); font-family: "Roboto", sans-serif; color: var(--muted); font-size: 5.4px; }
  .sidebar .item { position: absolute; left: 19px; white-space: nowrap; }
  .sidebar .label { color: var(--ink); font-weight: 500; }
  .sidebar .contact { display: flex; align-items: center; gap: 3px; }
  .sidebar .contact svg { width: 5px; height: 5px; }
  .sidebar .address { color: var(--ink); font-weight: 700; line-height: 7px; }
  .badge { position: absolute; border-radius: 50%; background: var(--badge); border: 2px solid #3a0a0e; }
  .sidebar .badge { left: 18px; top: 410px; width: 52px; height: 52px; }

  .brand { position: absolute; text-align: center; font-family: "Open Sans", sans-serif; font-weight: 600; color: var(--ink); line-height: 1; }
  .brand .name { font-size: 6.4px; letter-spacing: 0.3px; white-space: nowrap; }
  .brand .mark { font-size: 28px; letter-spacing: 1px; margin-top: 14px; }
  .brand .est { font-size: 4.6px; margin-top: 4px; letter-spacing: 1px; }
  .letterhead .brand { left: 234px; top: 26px; transform: translateX(-50%); }

  .watermark { position: absolute; text-align: center; font-family: "Open Sans", sans-serif; font-weight: 600; color: var(--watermark); line-height: 1; }
  .watermark .rule { border-top: 1.5px solid var(--watermark); border-radius: 50%; height: 14px; }
  .letterhead .watermark { left: 230px; top: 470px; width: 210px; }
  .letterhead .watermark .mark { font-size: 56px; margin-top: -4px; letter-spacing: 2px; }

  .letter { position: absolute; left: 111px; top: 116px; width: 290px; font-size: 7.6px; line-height: 14.6px; }
  .letter p { margin-bottom: 14.6px; }
  .letter .opening { margin-bottom: 16px; }
  .signature { width: 104px; height: 36px; border-radius: 18px; background: var(--signature); margin: -8px 0 6px; }

  /* Envelope front */
  .envelope-front { left: 578px; top: 42px; width: 556px; height: 254px; font-family: "Roboto", sans-serif; }
  .envelope-front .brand { left: 14px; top: 28px; }
  .envelope-front .brand .name { font-size: 4.4px; }
  .envelope-front .brand .mark { font-size: 17px; margin-top: 8px; }
  .envelope-front .brand .est { font-size: 3.4px; }
  .envelope-front .badge { left: 122px; top: 20px; width: 38px; height: 38px; }
  .envelope-front .address { position: absolute; left: 24px; top: 222px; font-size: 7px; line-height: 9px; color: var(--ink); }
  .envelope-front .watermark { left: 322px; top: 156px; width: 226px; }
  .envelope-front .watermark .mark { font-size: 64px; margin-top: -4px; letter-spacing: 2px; }

  /* Envelope back */
  .envelope-back { left: 578px; top: 344px; width: 556px; height: 254px; }
  .envelope-back .flap { position: absolute; left: 0; top: 0; width: 556px; height: 70px; }
  .envelope-back .brand { left: 278px; top: 22px; transform: translateX(-50%); }
  .envelope-back .brand .name { font-size: 4.4px; }
  .envelope-back .brand .mark { font-size: 16px; margin-top: 6px; }
  .envelope-back .brand .est { font-size: 3.4px; }
</style>
</head>
<body>
<main class="board">

  <section class="sheet letterhead" aria-label="Letterhead">
    <aside class="sidebar">
      <div class="item label" style="top:108px">partners:</div>
      <div class="item" style="top:126px">Dale K. Hollingsworth</div>
      <div class="item" style="top:142px">Vernon P. Hollingsworth</div>
      <div class="item" style="top:158px">Mark E. Fenwicke</div>
      <div class="item" style="top:174px">Tyler D. Ashcombe</div>
      <div class="item label" style="top:206px">Other staff:</div>
      <div class="item" style="top:223px">Brenda K. Lyle</div>
      <div class="item" style="top:239px">Tendaji K. Oyelowanta</div>
      <div class="item" style="top:255px">Gordon Pettijo</div>
      <div class="item" style="top:287px">Hilda V. Pruitt, RN</div>
      <div class="item label" style="top:319px">Of Counsel:</div>
      <div class="item" style="top:336px">Wendell S. Hollingsworth</div>
      <div class="badge" role="img" aria-label="Seven-Figure Verdict Logo"></div>
      <div class="item contact" style="top:479px">
        <svg viewBox="0 0 10 10"><path d="M1 3c0-1 1-2 4-2s4 1 4 2v1H7V3H3v1H1zM2 5h6l1 4H1z" fill="#222"/></svg>(918) 555-0143
      </div>
      <div class="item contact" style="top:489px">
        <svg viewBox="0 0 10 10"><rect x="1" y="4" width="8" height="5" fill="#222"/><rect x="3" y="1" width="4" height="3" fill="#222"/></svg>(918) 555-0187
      </div>
      <div class="item contact" style="top:499px">
        <svg viewBox="0 0 10 10"><circle cx="5" cy="5" r="4" fill="none" stroke="#222"/><path d="M1 5h8M5 1c-2 2-2 6 0 8M5 1c2 2 2 6 0 8" fill="none" stroke="#222" stroke-width="0.7"/></svg>www.TWVQX.example
      </div>
      <div class="item address" style="top:510px">5182 North Pelham Avenue<br>Tulsa, Oklahoma 74219</div>
    </aside>

    <div class="brand">
      <div class="name">HOLLINGSWORTH HOLLINGSWORTH FENWICKE</div>
      <div class="mark">HHF</div>
      <div class="est">EST 1984</div>
    </div>

    <div class="watermark" aria-hidden="true">
      <div class="rule"></div>
      <div class="mark">HHF</div>
    </div>

    <article class="letter">
      <p class="opening">Lorem Ipsum is simply</p>
      <p>dummy text of the printing and typesetting industry. Lorem Ipsum has been the industry's standard dummy text ever since the 1500s, when an unknown printer took a galley of type and scrambled it to make a type specimen book. It has survived not only five centuries, but also the leap into electronic typesetting, remaining essentially unchanged.</p>
      <p>It is a long established fact that a reader will be distracted by the readable content of a page when looking at its layout. The point of using Lorem Ipsum is that it has a more-or-less normal distribution of letters, as opposed to using 'Content here, content here', making it look like readable English.</p>
      <p>Contrary to popular belief, Lorem Ipsum is not simply random text. It has roots in a piece of classical Latin literature from 45 BC, making it over 2000 years old. Harold Penwarden, a Latin professor at Ashgrove College in Virginia, looked up one of the more obscure Latin words, consectetur, from a Lorem Ipsum passage, and going through the cites of the word in classical literature, discovered the undoubtable source. Lorem Ipsum comes from sections 1.10.32 and 1.10.33 of "de Finibus Bonorum et Malorum" (The Extremes of Good and Evil) by Varrus, written in 45 BC. This book</p>
      <p style="margin-bottom:12px">Lorem Ipsum</p>
      <div class="signature" role="img" aria-label="Handwritten signature"></div>
      <p>Lorem Ipsum is a dummy</p>
    </article>
  </section>

  <section class="sheet envelope-front" aria-label="Envelope front">
    <div class="brand">
      <div class="name">HOLLINGSWORTH HOLLINGSWORTH FENWICKE</div>
      <div class="mark">HHF</div>
      <div class="est">EST 1984</div>
    </div>
    <div class="badge" role="img" aria-label="Seven-Figure Verdict Logo"></div>
    <div class="watermark" aria-hidden="true">
      <div class="rule"></div>
      <div class="mark">HHF</div>
    </div>
    <div class="address">5182 North Pelham Avenue<br>Tulsa, Oklahoma 74219</div>
  </section>

  <section class="sheet envelope-back" aria-label="Envelope back">
    <svg class="flap" viewBox="0 0 556 70" aria-hidden="true">
      <path d="M0 0 C10 10 18 38 30 58 Q34 63 48 63 L508 63 Q522 63 526 58 C538 38 546 10 556 0" fill="none" stroke="#333" stroke-width="0.8"/>
    </svg>
    <div class="brand">
      <div class="name">HOLLINGSWORTH HOLLINGSWORTH FENWICKE</div>
      <div class="mark">HHF</div>
      <div class="est">EST 1984</div>
    </div>
  </section>

</main>
</body>
</html>
```